Branvique needs a business Card Design

We are looking for a business card Design for our new Managed Service Provider Company, Branvique. Branvique encompasses everything IT for the average medium sized business. Our primary services are help desk support, cyber-security (malware and ransomware protection), and Disaster Recovery systems. We would like the design to have a very clean and professional look, with a very minimalist feel.

Target Market(s)

Medium to large sized businesses

Industry/Entity Type

It Service

Contact Information for Business Card

Name GoesHere
name@branvique.com
O: 555-382-6047
C: 555-731-5820

Font styles to use
Other font styles liked:
• Poppins Font Only Please

Colors

Designer to choose only greyscale colors for use in the design.

Requirements
Must have
• Logo included
Nice to have
• Cutting Edge, innovative, minimalistic, elegant

```html
<!DOCTYPE html>
<html lang="en">
<head>
<meta charset="utf-8">
<title>Branvique Business Card</title>
<link rel="stylesheet" href="https://fonts.googleapis.com/css2?family=Poppins:ital,wght@0,300;0,400;0,600;1,300&display=swap">
<style>
  :root {
    --paper: #ffffff;
    --ink: #000000;
    --brand-navy: #0d2438;
    --band: #000000;
    --band-text: #ffffff;
    --caption: #111111;
  }
  * { margin: 0; padding: 0; box-sizing: border-box; }
  html, body {
    width: 1200px;
    height: 1000px;
    overflow: hidden;
    background: var(--paper);
    font-family: "Poppins", sans-serif;
  }
  .board {
    position: relative;
    width: 1200px;
    height: 1000px;
  }
  .card {
    position: absolute;
    width: 611px;
    height: 351px;
    border: 1px solid var(--ink);
    background: var(--paper);
    overflow: hidden;
  }
  .card--thumb {
    left: 118px;
    top: 101px;
    transform: scale(0.414);
    transform-origin: top left;
    border-width: 2.4px;
  }
  .card--main {
    left: 535px;
    top: 587px;
  }
  .card__brand {
    position: absolute;
    left: 0;
    top: 0;
    width: 100%;
    height: 239px;
  }
  .brand-square {
    position: absolute;
    left: 50%;
    top: 70px;
    width: 38px;
    height: 38px;
    margin-left: -19px;
    background: var(--brand-navy);
  }
  .brand-name {
    position: absolute;
    left: 0;
    top: 170px;
    width: 100%;
    text-align: center;
    font-size: 36px;
    font-weight: 400;
    letter-spacing: 0.5em;
    text-indent: 0.5em;
    color: var(--brand-navy);
    line-height: 1;
  }
  .card__band {
    position: absolute;
    left: 0;
    bottom: 0;
    width: 100%;
    height: 112px;
    background: var(--band);
    color: var(--band-text);
    text-align: right;
    padding: 12px 15px 0 0;
    font-size: 14px;
    line-height: 22px;
  }
  .contact__name { font-weight: 600; }
  .contact__email { font-weight: 300; font-style: italic; }
  .contact__phone { font-weight: 400; }
  .note {
    position: absolute;
    left: 118px;
    top: 664px;
    font-size: 17px;
    font-weight: 300;
    line-height: 23px;
    color: var(--caption);
  }
</style>
</head>
<body>
<main class="board">
  <article class="card card--thumb" aria-label="Business card, small preview">
    <div class="card__brand">
      <span class="brand-square"></span>
      <div class="brand-name">BRANVIQUE</div>
    </div>
    <div class="card__band">
      <div class="contact__name">Name Goes Here</div>
      <div class="contact__email">name@branvique.com</div>
      <div class="contact__phone">O: 555-382-6047</div>
      <div class="contact__phone">C: 555-731-5820</div>
    </div>
  </article>

  <p class="note">Leaves enough space for longer names<br>and longer email adresses</p>

  <article class="card card--main" aria-label="Business card">
    <div class="card__brand">
      <span class="brand-square"></span>
      <div class="brand-name">BRANVIQUE</div>
    </div>
    <div class="card__band">
      <div class="contact__name">Name Goes Here</div>
      <div class="contact__email">name@branvique.com</div>
      <div class="contact__phone">O: 555-382-6047</div>
      <div class="contact__phone">C: 555-731-5820</div>
    </div>
  </article>
</main>
</body>
</html>
```